Brellwick Finance Stationary Design

We have selected a logo as our winner, we now need a full stationary set to be in the same theme.
Required:
- Letter Head
- Business Card Template
- Custom Envelopes
- A5 Notepad Design (Front cover and content pages. Content pages blank(no lines) but with our branding on them,)
- With Compliments Slip
Updates

Hey All,

We have changed the colour scheme of our logo. Our apologies if anyone has begun designing based off the old scheme. Please see the updated scheme in the brief,

Tobin

Target Market(s)

Target market is experienced property developers and financial institutions.

Industry/Entity Type

Commercial Finance

Font styles to use
Serif

Colors
0054AA
0677BA
7BADD7
CADEEF
E8F1F8
0094D4
00A9DD
6FCCEA
C7EBF8
E9F6FB
00AB8E
00BBA5
67D7C9
C6EFE9
E9F9F6
59FF00
82FF00
B8FF75
E3FFCB
F4FFEA

```html
<!DOCTYPE html>
<html lang="en">
<head>
<meta charset="utf-8">
<title>Brellwick Finance – Business Card</title>
<link href="https://fonts.googleapis.com/css2?family=Arimo:wght@400;700&family=Roboto+Condensed:wght@600&display=swap" rel="stylesheet">
<style>
  :root {
    --brand-blue: #003399;
    --brand-green: #1f7f38;
    --paper: #f6f6f8;
    --backdrop: #e4e4e4;
    --ink-light: #ffffff;
  }
  * { margin: 0; padding: 0; box-sizing: border-box; }
  html, body { width: 1200px; height: 1200px; overflow: hidden; }
  body {
    background: var(--backdrop);
    font-family: "Arimo", Arial, sans-serif;
    position: relative;
  }
  .card {
    position: absolute;
    left: 262px;
    width: 686px;
    height: 392px;
    overflow: hidden;
  }
  .card--front { top: 165px; background: var(--paper); }
  .card--back { top: 653px; background: var(--brand-blue); }

  .wordmark {
    position: absolute;
    left: 0; right: 0;
    text-align: center;
    font-family: "Arimo", Arial, sans-serif;
    font-weight: 700;
    letter-spacing: 2px;
    text-transform: uppercase;
    line-height: 1;
  }
  .card--front .wordmark { top: 80px; font-size: 44px; color: var(--brand-blue); }
  .card--back .wordmark { top: 170px; font-size: 48px; color: var(--ink-light); }

  .accent-rule {
    position: absolute;
    left: 0; right: 0;
    top: 201px;
    height: 6px;
    background: var(--brand-green);
  }
  .contact-band {
    position: absolute;
    left: 0; right: 0;
    top: 209px;
    bottom: 0;
    background: var(--brand-blue);
    color: var(--ink-light);
  }
  .identity {
    position: absolute;
    right: 353px;
    top: 35px;
    text-align: right;
    font-size: 16.5px;
    line-height: 21px;
  }
  .identity .person-name {
    font-family: "Roboto Condensed", "Arial Narrow", sans-serif;
    font-weight: 600;
    font-size: 24px;
    line-height: 26px;
    margin-bottom: 1px;
  }
  .divider {
    position: absolute;
    left: 346px;
    top: 38px;
    width: 1px;
    height: 82px;
    background: rgba(255,255,255,0.45);
  }
  .contact-list {
    position: absolute;
    left: 357px;
    top: 38px;
    list-style: none;
    font-size: 16.5px;
    line-height: 20.5px;
  }
  .contact-list li { display: flex; align-items: center; gap: 8px; }
  .contact-list svg { width: 14px; height: 14px; flex: none; }
</style>
</head>
<body>

  <section class="card card--front">
    <div class="wordmark">Brellwick Finance</div>
    <div class="accent-rule"></div>
    <div class="contact-band">
      <div class="identity">
        <div class="person-name">MARTIN HALE</div>
        <div>Managing Director</div>
        <div>4120 Alder Court</div>
        <div>Fairbanks, Alaska 99701</div>
      </div>
      <div class="divider"></div>
      <ul class="contact-list">
        <li>
          <svg viewBox="0 0 16 16" aria-hidden="true"><path fill="#fff" d="M3.6 1.2l2.3 2.8-1.4 1.7c.9 2 2.6 3.7 4.6 4.6l1.7-1.4 2.8 2.3-1.4 2.3C7 13.2 2.8 9 1.3 2.6z"/></svg>
          555-214-7830
        </li>
        <li>
          <svg viewBox="0 0 16 16" aria-hidden="true"><rect x="4" y="1" width="8" height="14" rx="1.2" fill="none" stroke="#fff" stroke-width="1.8"/><rect x="7" y="12" width="2" height="1.4" fill="#fff"/></svg>
          555-309-6418
        </li>
        <li>
          <svg viewBox="0 0 16 16" aria-hidden="true"><rect x="1" y="3.5" width="14" height="9" fill="#fff"/><path d="M1.5 4l6.5 5 6.5-5" fill="none" stroke="#003399" stroke-width="1.3"/></svg>
          info@brellwickfinance.com
        </li>
        <li>
          <svg viewBox="0 0 16 16" aria-hidden="true"><circle cx="8" cy="8" r="7" fill="#fff"/><path d="M8 1v14M1 8h14M8 1c-3 3-3 11 0 14M8 1c3 3 3 11 0 14" fill="none" stroke="#003399" stroke-width="1"/></svg>
          www.brellwickfinance.com
        </li>
      </ul>
    </div>
  </section>

  <section class="card card--back">
    <div class="wordmark">Brellwick Finance</div>
  </section>

</body>
</html>
```